Window Wrap advertising for Insurance Agency
Pinegate Coverage Partners
Window Wrap advertising for Insurance Agency - Financial Services
We are an insurance agency specializing in Auto, Home, Life and Business insurance and we are looking to update the graphics and messaging of some window wraps that we have on our building. We currently have 6 windows wrapped but are now wanting to wrap a total of 8 windows. they are of various sizes, so I am providing an .ai file with the appropriately sized artboards to make things a little easier. The .ai file will also show you what our previous wraps looked like. We do not like anything about our old design, so please do not rely too heavily on it. The windows that these wraps will go on are facing a fairly busy street and we want some messaging on these wraps that will entice potential clients to come in or call us to get insurance quotes. Walk-ins are welcome at our office. We really want to see ideas that are eye-catching, and have a great call to action.
Financial Services
All members of the public who drive cars, own homes, own businesses or need life insurance ( which is to say, almost everyone.)
Velmora Velmora
Hello why you make it unvield? Please make it veild again so that other designer can not see our designs, this is very simportant so that we assure that no one copy other ideas. And please also provide text content for each window. Thanks
tallowk58 tallowk58
Hello designers, Thank you for your submissions. I would like to clarify a few things. First of all, there are a total of 8 windows... In the ai file that I attached, there are 8 art boards. Although there are 3 blank art boards, we need all 8 to be designed. Second, we HATE our current window designs. Please do not use any of the design cues from the current windows. The only logo that we want included somewhere is our own logo which I have also attached. I'd like to reiterate that we want to see eye catching designs that will help draw in traffic. And text on the windows needs to be fairly large so that it can bee seen from the street. If you have questions, please feel free to send me a message. Thanks again for your designs.

```html
<!DOCTYPE html>
<html lang="en">
<head>
<meta charset="utf-8">
<title>Pinegate Coverage Partners – Window Wraps</title>
<link rel="stylesheet" href="https://fonts.googleapis.com/css2?family=PT+Serif:wght@400;700&display=swap">
<style>
  :root{
    --navy:#1c2858;
    --navy-deep:#0f1638;
    --red:#9a1c22;
    --paper:#ffffff;
    --silver:#d9d9dd;
    --silver-deep:#b9bac2;
    --photo-a:#8a8f9a;
    --photo-b:#c9b9a6;
  }
  *{box-sizing:border-box;margin:0;padding:0}
  html,body{width:1200px;height:830px;overflow:hidden;background:var(--paper)}
  body{position:relative;font-family:"PT Serif",Georgia,serif;color:var(--navy)}

  .wrap{position:absolute;overflow:hidden;
    background:linear-gradient(180deg,#fff 0%,#f1f1f3 45%,var(--silver) 80%,var(--silver-deep) 100%);
    box-shadow:0 2px 6px rgba(0,0,0,.25)}

  .wrap__photo{position:absolute;left:4%;right:4%;top:3%;height:46%;
    border-radius:0 0 50% 50% / 0 0 38% 38%;
    background:linear-gradient(160deg,var(--photo-a),var(--photo-b))}

  .wrap__swoosh{position:absolute;inset:0;width:100%;height:100%;pointer-events:none}

  .wrap__logo{position:absolute;top:3%;right:4%;display:flex;align-items:center;gap:4px;
    background:rgba(255,255,255,.92);border-radius:14px;padding:3px 7px}
  .wrap__logo-dot{width:11px;height:11px;border-radius:50%;background:var(--red);flex:none}
  .wrap__logo-name{font-size:7px;font-weight:700;color:var(--navy);line-height:1.1;max-width:62px}

  .wrap__icon{position:absolute;border-radius:50%;
    background:radial-gradient(circle at 40% 40%,#f3f3f3,#9ea3ad);box-shadow:0 1px 3px rgba(0,0,0,.3)}

  .wrap__copy{position:absolute;right:6%;text-align:right;line-height:1.05}
  .wrap__copy--center{left:5%;right:5%;text-align:center}
  .t-small{display:block;font-size:13px;color:var(--red)}
  .t-mid{display:block;font-size:20px;color:var(--navy)}
  .t-big{display:block;font-size:26px;color:var(--navy)}
  .t-red{color:var(--red);text-transform:uppercase}

  .wrap__band{position:absolute;left:0;right:0;bottom:0;height:11%;
    background:linear-gradient(180deg,#3a4678,var(--navy-deep));
    display:flex;align-items:center;justify-content:center;
    color:#fff;font-weight:700;text-transform:uppercase;letter-spacing:1px;font-size:20px}
</style>
</head>
<body>

<svg width="0" height="0" style="position:absolute">
  <defs>
    <symbol id="swoosh" viewBox="0 0 100 100" preserveAspectRatio="none">
      <path d="M0 4 Q40 -2 70 6 Q96 14 100 34 L100 26 Q92 8 66 2 Q34 -4 0 0 Z" fill="#1c2858"/>
      <path d="M0 8 Q44 2 74 10 Q98 20 100 44 L100 36 Q94 14 70 7 Q36 0 0 5 Z" fill="#9a1c22"/>
      <path d="M0 44 Q50 58 100 42 L100 45 Q50 61 0 47 Z" fill="#9a1c22"/>
      <path d="M0 48 Q50 62 100 46 L100 48.5 Q50 64.5 0 50.5 Z" fill="#1c2858"/>
    </symbol>
  </defs>
</svg>

<!-- Business -->
<section class="wrap" style="left:19px;top:24px;width:317px;height:360px">
  <div class="wrap__photo" role="img" aria-label="Photo of business people meeting around a table"></div>
  <svg class="wrap__swoosh"><use href="#swoosh"/></svg>
  <div class="wrap__logo"><span class="wrap__logo-dot"></span><span class="wrap__logo-name">Pinegate Coverage Partners</span></div>
  <div class="wrap__icon" style="left:7%;top:62%;width:58px;height:40px" role="img" aria-label="Small image of coins and money"></div>
  <div class="wrap__copy" style="top:64%"><span class="t-mid">safe your business</span><span class="t-big">from now</span></div>
  <div class="wrap__band">Business</div>
</section>

<!-- Auto -->
<section class="wrap" style="left:355px;top:24px;width:281px;height:360px">
  <div class="wrap__photo" role="img" aria-label="Photo of a worried driver beside a damaged car"></div>
  <svg class="wrap__swoosh"><use href="#swoosh"/></svg>
  <div class="wrap__logo"><span class="wrap__logo-dot"></span><span class="wrap__logo-name">Pinegate Coverage Partners</span></div>
  <div class="wrap__icon" style="left:5%;top:71%;width:62px;height:40px" role="img" aria-label="Small image of a car with a shield"></div>
  <div class="wrap__copy" style="top:61%"><span class="t-small">don't be affraid!</span><span class="t-mid">Get your</span><span class="t-mid t-red">car insurance</span><span class="t-mid">today</span></div>
  <div class="wrap__band">Auto</div>
</section>

<!-- Home -->
<section class="wrap" style="left:660px;top:29px;width:192px;height:283px">
  <div class="wrap__photo" role="img" aria-label="Photo of a house with a lawn and sky"></div>
  <svg class="wrap__swoosh"><use href="#swoosh"/></svg>
  <div class="wrap__logo"><span class="wrap__logo-dot"></span><span class="wrap__logo-name">Pinegate Coverage Partners</span></div>
  <div class="wrap__icon" style="left:5%;top:64%;width:44px;height:40px" role="img" aria-label="Small image of an umbrella over a house"></div>
  <div class="wrap__copy" style="top:60%"><span class="t-small" style="font-size:10px">for your solution</span><span class="t-mid" style="font-size:14px">Get your</span><span class="t-mid t-red" style="font-size:14px">home<br>insurance</span><span class="t-mid" style="font-size:14px">today</span></div>
  <div class="wrap__band" style="font-size:16px">Home</div>
</section>

<!-- Health -->
<section class="wrap" style="left:876px;top:24px;width:305px;height:360px">
  <div class="wrap__photo" role="img" aria-label="Photo of an injured man resting with a bandaged arm"></div>
  <svg class="wrap__swoosh"><use href="#swoosh"/></svg>
  <div class="wrap__logo"><span class="wrap__logo-dot"></span><span class="wrap__logo-name">Pinegate Coverage Partners</span></div>
  <div class="wrap__icon" style="left:6%;top:64%;width:58px;height:42px" role="img" aria-label="Small image of a heart and pills"></div>
  <div class="wrap__copy" style="top:61%"><span class="t-small">don't be affraid!</span><span class="t-mid">Get your</span><span class="t-mid t-red">health insurance</span><span class="t-mid">today</span></div>
  <div class="wrap__band">Health</div>
</section>

<!-- Life -->
<section class="wrap" style="left:19px;top:444px;width:317px;height:360px">
  <div class="wrap__photo" role="img" aria-label="Photo of a smiling family together"></div>
  <svg class="wrap__swoosh"><use href="#swoosh"/></svg>
  <div class="wrap__logo"><span class="wrap__logo-dot"></span><span class="wrap__logo-name">Pinegate Coverage Partners</span></div>
  <div class="wrap__icon" style="left:7%;top:68%;width:52px;height:40px" role="img" aria-label="Small image of a family group"></div>
  <div class="wrap__copy" style="top:62%"><span class="t-small">save your family</span><span class="t-big">save</span><span class="t-big t-red">your life</span></div>
  <div class="wrap__band">Life</div>
</section>

<!-- Travel -->
<section class="wrap" style="left:360px;top:504px;width:180px;height:228px">
  <div class="wrap__photo" role="img" aria-label="Photo of a map with a passport and plane"></div>
  <svg class="wrap__swoosh"><use href="#swoosh"/></svg>
  <div class="wrap__logo"><span class="wrap__logo-dot"></span><span class="wrap__logo-name">Pinegate Coverage Partners</span></div>
  <div class="wrap__copy" style="top:62%"><span class="t-small" style="font-size:10px;color:var(--navy)">to safe your travel</span><span class="t-mid" style="font-size:15px">Get <span class="t-red">insurance</span></span><span class="t-mid" style="font-size:15px">today</span></div>
  <div class="wrap__band" style="font-size:13px">Travel</div>
</section>

<!-- Liability -->
<section class="wrap" style="left:559px;top:444px;width:209px;height:360px">
  <div class="wrap__photo" role="img" aria-label="Photo of a person in a suit holding an insurance form"></div>
  <svg class="wrap__swoosh"><use href="#swoosh"/></svg>
  <div class="wrap__logo"><span class="wrap__logo-dot"></span><span class="wrap__logo-name">Pinegate Coverage Partners</span></div>
  <div class="wrap__copy wrap__copy--center" style="top:66%"><span class="t-mid">Get <span class="t-red">insurance</span></span><span class="t-mid">today</span><span class="t-small" style="color:var(--navy)">to safe your life</span></div>
  <div class="wrap__band" style="font-size:16px">Liability</div>
</section>

<!-- Legal expences -->
<section class="wrap" style="left:787px;top:444px;width:197px;height:360px">
  <div class="wrap__photo" role="img" aria-label="Photo of a large legal section symbol"></div>
  <svg class="wrap__swoosh"><use href="#swoosh"/></svg>
  <div class="wrap__logo"><span class="wrap__logo-dot"></span><span class="wrap__logo-name">Pinegate Coverage Partners</span></div>
  <div class="wrap__copy wrap__copy--center" style="top:66%"><span class="t-mid">Get <span class="t-red">insurance</span></span><span class="t-mid">today</span><span class="t-small" style="color:var(--navy)">to safe your life</span></div>
  <div class="wrap__band" style="font-size:14px">Legal expences</div>
</section>

</body>
</html>
```